Copper Ridge Inquiries Letterhead

I would like to design a letterhead for a private investigation company. Our primary clients will be law firms. The business card is included below

```html
<!DOCTYPE html>
<html lang="en">
<head>
<meta charset="utf-8">
<title>Copper Ridge Inquiries – Letterhead</title>
<link rel="stylesheet" href="https://fonts.googleapis.com/css2?family=Montserrat:wght@400;500;700&display=swap">
<style>
  :root {
    --navy: #1d3260;
    --orange: #f05a2a;
    --body-grey: #5a5d63;
    --backdrop: #d9d9db;
    --paper: #ffffff;
    --signature-tone: #e8e8ea;
  }
  * { margin: 0; padding: 0; box-sizing: border-box; }
  html, body {
    width: 1200px; height: 960px; overflow: hidden;
    background: var(--backdrop);
    font-family: "Montserrat", Arial, sans-serif;
  }
  .letterhead {
    position: absolute; left: 260px; top: 40px;
    width: 680px; height: 880px;
    background: var(--paper);
    border-bottom: 5px solid var(--orange);
  }
  .brand {
    position: absolute; left: 56px; top: 58px;
    display: flex; align-items: center; gap: 10px;
  }
  .brand-dot {
    width: 14px; height: 14px; border-radius: 50%;
    background: var(--orange);
  }
  .brand-name {
    font-weight: 700; font-size: 20px; letter-spacing: 0.5px;
    color: var(--navy); text-transform: uppercase;
  }
  .letter {
    position: absolute; left: 96px; top: 186px; width: 470px;
  }
  .salutation {
    font-size: 15px; font-weight: 500; color: var(--navy);
    margin-bottom: 20px;
  }
  .letter-body p {
    font-size: 11px; line-height: 1.45; color: var(--body-grey);
    margin-bottom: 22px;
  }
  .sign-off {
    margin-top: 36px; margin-left: 150px;
  }
  .closing { font-size: 11px; color: var(--body-grey); }
  .signature-mark {
    display: block; width: 80px; height: 14px; margin: 4px 0 8px 18px;
    background: var(--signature-tone); border-radius: 2px;
  }
  .signer { font-size: 11px; color: var(--body-grey); text-transform: uppercase; }
  .contact-block {
    position: absolute; right: 40px; bottom: 52px; width: 380px;
    font-size: 11px; font-style: normal; color: var(--body-grey);
    text-transform: uppercase;
  }
  .contact-row { display: flex; align-items: center; gap: 8px; }
  .contact-item { display: flex; align-items: center; gap: 5px; }
  .contact-gap { width: 14px; }
  .contact-rule {
    height: 2px; background: var(--orange); margin: 8px 0;
  }
  .icon { width: 10px; height: 10px; fill: var(--orange); flex: none; }
</style>
</head>
<body>
  <main class="letterhead">
    <header class="brand">
      <span class="brand-dot"></span>
      <span class="brand-name">Copper Ridge Inquiries</span>
    </header>

    <article class="letter">
      <p class="salutation">Dear Mr. Halvorsen</p>

      <section class="letter-body">
        <p>Lorem Ipsum is simply dummy text of the printing and typesetting industry. Lorem Ipsum has been the industry's standard dummy text ever since the 1500s, when an unknown printer took a galley of type and scrambled it to make a type specimen book. It has survived not only five centuries, but also the leap into electronic typesetting, remaining essentially unchanged. It was popularised in the 1960s with the release of Letraset sheets containing Lorem Ipsum passages</p>
        <p>Lorem Ipsum is simply dummy text of the printing and typesetting industry. Lorem Ipsum has been the industry's standard dummy text ever since the 1500s, when an unknown printer took a galley of type and scrambled it to make a type specimen book. It has survived not only five centuries, but also the leap into electronic typesetting, remaining essentially unchanged. It was popularised in the 1960s with the release of Letraset sheets containing Lorem Ipsum passages</p>
        <p>Lorem Ipsum is simply dummy text of the printing and typesetting industry. Lorem Ipsum has been the industry's standard dummy text ever since the 1500s, when an unknown printer took a galley of type and scrambled it to make a type specimen book. It has survived not only five centuries, but also the leap into electronic typesetting, remaining essentially unchanged. It was popularised in the 1960s with the release of Letraset sheets containing Lorem Ipsum passages</p>
      </section>

      <footer class="sign-off">
        <p class="closing">Sincerely</p>
        <span class="signature-mark" role="img" aria-label="Handwritten signature"></span>
        <p class="signer">Daniel Fairwick</p>
      </footer>
    </article>

    <address class="contact-block">
      <div class="contact-row">
        <span class="contact-item">
          <svg class="icon" viewBox="0 0 10 10" aria-hidden="true"><path d="M5 0a3.6 3.6 0 0 0-3.6 3.6C1.4 6.3 5 10 5 10s3.6-3.7 3.6-6.4A3.6 3.6 0 0 0 5 0zm0 5a1.4 1.4 0 1 1 0-2.8A1.4 1.4 0 0 1 5 5z"/></svg>
          Silver Falls, NV
        </span>
        <span class="contact-gap"></span>
        <span>License No. 04427153</span>
      </div>
      <div class="contact-rule"></div>
      <div class="contact-row">
        <span class="contact-item">
          <svg class="icon" viewBox="0 0 10 10" aria-hidden="true"><path d="M2 .5l1.8 2-1 1.2a6 6 0 0 0 3.5 3.5l1.2-1 2 1.8-1 1.5C4.5 9.5.5 5.5.5 1.5z"/></svg>
          555.314.2790
        </span>
        <span class="contact-item">
          <svg class="icon" viewBox="0 0 10 10" aria-hidden="true"><path d="M0 2h10v6H0zM.8 2.6 5 5.6l4.2-3H.8z"/></svg>
          office@copperridgeinquiries.com
        </span>
      </div>
    </address>
  </main>
</body>
</html>
```